The Steady Climb Podcast Cover Art

I'm upgrading my podcast cover art to a new design. The show is called The Steady Climb and we interview guests who have gone through different challenges/adversities that we face in life. During the interview, we unpack how they've gotten past the adversity and how that insight might help others. I will link the show and old cover art. I will upload a new photo or two that can be used for the new cover art.

Look at previous cover for items that needed on the cover like Podvara, wavlio etc.

Should also have a small caption that states
“UNTOLD STORIES OF EVERYDAY ADVERSITY & PERSEVERANCE”

Wavlio: https://listen.wavlio-example.net/show/7QR2k4LdPzHwXnBTVmcaF9?si=ra4Xk8Tpqe-W27YbCvhnpL

Target Market(s)

Podcast learning community

Industry/Entity Type

Podcast, Education

Colors
EB3D1F
EC4F4E
F09395
F8D3D4
FCEDEE

Requirements
Must have
• RM Logo, Colors are red, black and white.

```html
<!DOCTYPE html>
<html lang="en">
<head>
<meta charset="utf-8">
<title>The Steady Climb – Podcast Cover</title>
<link rel="stylesheet" href="https://fonts.googleapis.com/css2?family=Bebas+Neue&family=Montserrat:wght@400;500&family=Mrs+Saint+Delafield&display=swap">
<style>
  :root {
    --page-bg: #1f1a28;
    --cover-light: #4b3f5c;
    --cover-dark: #342a43;
    --title-white: #ffffff;
    --title-orange: #ff6500;
    --silhouette: #050507;
    --jumper-tone: #1c1826;
    --blazer-tone: #554866;
    --shirt-tone: #ece9f0;
    --caption: #ffffff;
  }
  * { margin: 0; padding: 0; box-sizing: border-box; }
  html, body {
    width: 768px; height: 1200px; overflow: hidden;
    background: var(--page-bg);
  }
  .cover {
    position: absolute; left: 0; top: 216px;
    width: 768px; height: 768px; overflow: hidden;
    background: radial-gradient(circle at 35% 55%, var(--cover-light) 0%, var(--cover-dark) 75%);
  }
  .title {
    position: absolute; left: 68px; top: 44px;
    font-family: "Bebas Neue", sans-serif; font-weight: 400;
  }
  .title__lead {
    display: block; font-size: 82px; line-height: 0.88;
    margin-bottom: 20px; color: var(--title-white);
  }
  .title__main {
    display: block; font-size: 131px; line-height: 0.88;
    margin-bottom: 6px; color: var(--title-orange);
  }
  .host-line {
    position: absolute; left: 68px; top: 384px;
    font-family: "Mrs Saint Delafield", cursive;
    font-size: 56px; color: var(--title-white); white-space: nowrap;
  }
  .cliff { position: absolute; background: var(--silhouette); }
  .cliff--left {
    left: 0; top: 620px; width: 278px; height: 148px;
    border-radius: 0 30px 0 0;
  }
  .cliff--right {
    left: 419px; top: 548px; width: 349px; height: 220px;
    border-radius: 18px 40px 0 0;
  }
  .jumper {
    position: absolute; left: 300px; top: 462px; width: 80px; height: 100px;
    background: radial-gradient(ellipse at 50% 50%, rgba(28,24,38,0.85) 0%, rgba(28,24,38,0.45) 45%, rgba(28,24,38,0) 72%);
  }
  .host-photo {
    position: absolute; left: 452px; top: 64px; width: 290px; height: 704px;
    border-radius: 120px 120px 0 0;
    background:
      linear-gradient(180deg,
        rgba(85,72,102,0) 0%,
        rgba(85,72,102,0.75) 22%,
        var(--blazer-tone) 38%,
        #8e839b 58%,
        var(--shirt-tone) 78%,
        var(--shirt-tone) 100%);
  }
  .brand {
    position: absolute; right: 27px; top: 104px;
    display: flex; align-items: center; gap: 7px;
    font-family: "Montserrat", sans-serif; font-weight: 500;
    font-size: 11px; letter-spacing: 0.6px; color: var(--title-white);
  }
  .brand__mark { width: 10px; height: 10px; background: var(--title-white); }
  .tagline {
    position: absolute; left: 68px; top: 690px;
    padding-left: 18px; border-left: 2px solid var(--caption);
    font-family: "Montserrat", sans-serif; font-weight: 400;
    font-size: 17px; line-height: 1.47; letter-spacing: 0.8px;
    color: var(--caption);
  }
</style>
</head>
<body>
  <main class="cover">
    <div class="cliff cliff--left" role="img" aria-label="Black silhouette of a rocky cliff edge"></div>
    <div class="cliff cliff--right" role="img" aria-label="Black silhouette of a rocky cliff on the far side of the gap"></div>
    <div class="jumper" role="img" aria-label="Silhouette of a person leaping between cliffs"></div>
    <div class="host-photo" role="img" aria-label="Photo of the host standing in a grey blazer, white t-shirt and white trousers"></div>

    <h1 class="title">
      <span class="title__lead">THE</span>
      <span class="title__main">STEADY</span>
      <span class="title__main">CLIMB</span>
    </h1>
    <p class="host-line">with Reese Marlow</p>

    <div class="brand"><span class="brand__mark"></span>REESE MARLOW</div>

    <p class="tagline">UNTOLD STORIES OF EVERYDAY<br>ADVERSITY &amp; PERSEVERANCE</p>
  </main>
</body>
</html>
```